Glow-Mist
Your Source for Stealth Vaping Solutions
I need double sided standard sized Business Card [3.5" x 2"]
I'll leave this up to you, play around w/ some different fonts.Keep it professional. I'm a retailer
Professional
Norris Pellgrave
CEO
Do not list an address on the card.
glowmist.staff@kelvora-mail.net
www.cirro-Q.net
A word about my business: We are a web-based retailer which specializes in electronic cigarettes. I'd like the card to look very professional and clean.
Black should be the dominant color in the scheme, or at least the background. If you can add a subtle pattern into the background that would be nice.
identical background, With a fullsized Cirro-Q logo displayed
Cirro-Q logo
the symbol by itself
this is the variation I want used.

```html
<!DOCTYPE html>
<html lang="en">
<head>
<meta charset="utf-8">
<title>Cirro-Q Business Card</title>
<link rel="stylesheet" href="https://fonts.googleapis.com/css2?family=Arimo:wght@400&display=swap">
<style>
  :root {
    --page: #1c1c1e;
    --card: #0b0b0c;
    --smoke-a: rgba(96, 128, 190, 0.38);
    --smoke-b: rgba(60, 84, 140, 0.18);
    --accent: #4a90c8;
    --rule: #5a5f68;
    --badge: #3a3f48;
    --text-light: #f2f2f2;
  }
  * { box-sizing: border-box; margin: 0; padding: 0; }
  html, body {
    width: 1200px; height: 1052px; overflow: hidden;
    background: var(--page);
    font-family: "Arimo", Arial, sans-serif;
  }
  .sheet {
    width: 1200px; height: 1052px;
    display: flex; flex-direction: column; align-items: center; justify-content: center;
    gap: 30px;
  }
  .card {
    position: relative;
    width: 860px; height: 491px;
    background: var(--card);
    overflow: hidden;
    box-shadow: 0 8px 24px rgba(0,0,0,0.5);
  }
  .smoke { position: absolute; inset: 0; }
  .card--front .smoke {
    background:
      radial-gradient(ellipse 22% 40% at 56% 35%, var(--smoke-a), transparent 70%),
      radial-gradient(ellipse 30% 45% at 70% 70%, var(--smoke-b), transparent 75%),
      radial-gradient(ellipse 18% 50% at 38% 55%, var(--smoke-b), transparent 70%);
  }
  .card--back .smoke {
    background:
      radial-gradient(ellipse 20% 55% at 58% 45%, var(--smoke-a), transparent 70%),
      radial-gradient(ellipse 22% 40% at 30% 30%, var(--smoke-b), transparent 72%),
      radial-gradient(ellipse 25% 45% at 82% 75%, var(--smoke-b), transparent 75%);
  }
  .edge-rule {
    position: absolute; top: 0; left: 56px;
    width: 2px; height: 100%;
    background: var(--rule);
  }

  .brand {
    position: absolute; left: 0; right: 0; top: 160px;
    display: flex; flex-direction: column; align-items: center; gap: 28px;
  }
  .brand-dot {
    width: 80px; height: 80px; border-radius: 50%;
    background: var(--badge);
  }
  .brand-name {
    color: var(--text-light);
    font-size: 64px; font-weight: 400;
    letter-spacing: 0;
  }

  .person {
    position: absolute; right: 48px; top: 62px; text-align: right;
  }
  .person-name { color: var(--text-light); font-size: 28px; }
  .person-role { color: var(--accent); font-size: 18px; margin-top: 6px; }

  .contact {
    position: absolute; left: 110px; bottom: 58px;
    color: var(--text-light); font-size: 24px; line-height: 1.45;
  }
</style>
</head>
<body>
<main class="sheet">
  <section class="card card--front">
    <div class="smoke" role="img" aria-label="Wisps of blue smoke drifting across a black background"></div>
    <div class="edge-rule"></div>
    <div class="brand">
      <div class="brand-dot"></div>
      <div class="brand-name">Cirro-Q</div>
    </div>
  </section>

  <section class="card card--back">
    <div class="smoke" role="img" aria-label="Wisps of blue smoke drifting across a black background"></div>
    <div class="edge-rule"></div>
    <div class="person">
      <p class="person-name">Norris Pellgrave</p>
      <p class="person-role">CEO</p>
    </div>
    <div class="contact">
      <p>(555) 014-7730</p>
      <p>www.cirro-Q.net</p>
      <p>glowmist.staff@kelvora-mail.net</p>
    </div>
  </section>
</main>
</body>
</html>
```